sailbrightly Website for children with diabilities

Hi, we are looking for a new website design for our community service "sailbrightly". Sailbrightly gives children who suffer from diseases or disabilities a week off on a Boat to give the children new hope and an unforgettable experience.

The current website is really old and we want to have a new one.
Please feel free to discover our website under http://sailbrightly-example.at/.
We have several company sponsors which are very important to us.

The Website has to be a Bootstrap Design (Version 4.4 or higher) [NOT Wordpress, Joomla, other CMS]

Target Market(s)

no target market. we like to inform our communities about our service.

Industry/Entity Type

community service for children with disabilities

Coding

Number of Pages Required

4 page

Font styles to use
Sans Serif

Colors
0054AA
0677BA
7BADD7
CADEEF
E8F1F8
0094D4
00A9DD
6FCCEA
C7EBF8
E9F6FB

Requirements
Must have
• About, Sponsors, Information about cruises
Nice to have
• Gallery

```html
<!DOCTYPE html>
<html lang="en">
<head>
<meta charset="utf-8">
<title>Sailbrightly – Community service for children with disabilities</title>
<link rel="stylesheet" href="https://fonts.googleapis.com/css2?family=Poppins:wght@400;500;600;700&family=Roboto:wght@400;500;700&display=swap">
<style>
:root{
  --page:#eaf3fb;
  --navy:#17226c;
  --navy-deep:#0f1a5a;
  --navy-soft:#2a3a8e;
  --ink:#1c1c24;
  --text:#4a4f66;
  --red:#d32a2a;
  --dark:#1b1d24;
  --white:#ffffff;
  --sea:#2a5c96;
  --sky:#7badd7;
}
*{box-sizing:border-box;margin:0;padding:0}
html,body{width:1200px;height:5396px;overflow:hidden}
body{background:var(--page);font-family:"Poppins",sans-serif;color:var(--ink);position:relative}
.abs{position:absolute}
.photo{position:absolute}
.framed{position:absolute;background:var(--white);padding:12px;box-shadow:0 4px 14px rgba(20,30,80,.18)}
.framed .fill{width:100%;height:100%}

/* header */
.site-header{position:absolute;left:0;top:0;width:1200px;height:147px;background:var(--page)}
.brand{position:absolute;left:73px;top:12px;width:120px;height:120px;border-radius:50%;background:var(--navy);display:flex;align-items:center;justify-content:center;color:var(--white);font-weight:600;font-size:15px}
.call{position:absolute;left:727px;top:38px;display:flex;align-items:center;gap:10px;font-size:11px;line-height:13px;font-weight:500}
.call .ico{width:28px;height:28px;border-radius:50%;background:var(--navy);display:flex;align-items:center;justify-content:center}
.lang{position:absolute;left:858px;top:42px;display:flex;align-items:center;gap:8px;font-size:12px;color:var(--text)}
.lang .flag{width:24px;height:24px;border-radius:50%;background:var(--navy)}
.btn-donate{position:absolute;display:flex;align-items:center;justify-content:space-between;padding:0 10px 0 32px;border-radius:22px;background:var(--navy);color:var(--white);font-size:12px;letter-spacing:.5px}
.btn-donate .arr{width:44px;height:30px;border-radius:15px;display:flex;align-items:center;justify-content:center}
.main-nav{position:absolute;top:96px;left:0;font-size:13px;color:var(--ink)}
.main-nav a{position:absolute;white-space:nowrap;color:inherit;text-decoration:none}
.main-nav a.active::after{content:"";position:absolute;left:0;right:0;top:26px;height:2px;background:var(--navy)}

/* hero */
.hero{position:absolute;left:0;top:147px;width:1200px;height:722px;overflow:hidden}
.hero .photo{inset:0;background:linear-gradient(180deg,#9fb7d0 0%,#6a8db4 25%,#3a6797 45%,#2b4f7a 70%,#203c63 100%)}
.hero-copy{position:absolute;left:71px;top:265px;color:var(--white)}
.hero-copy .pre{font-size:29px;letter-spacing:5px;font-weight:400}
.hero-copy h1{font-size:50px;font-weight:700;line-height:60px;margin-top:4px}
.hero-copy p{font-size:15px;margin-top:4px}
.hero .slide-arrow{position:absolute;top:352px;width:30px;height:30px;border-radius:50%;background:rgba(255,255,255,.35);display:flex;align-items:center;justify-content:center}

.section-title{position:absolute;left:0;width:1200px;text-align:center;font-size:32px;font-weight:600;color:var(--ink)}

/* about */
.about-block h3{position:absolute;left:637px;font-size:30px;font-weight:600}
.about-block h3::after{content:"";position:absolute;left:0;top:52px;width:60px;height:3px;background:var(--red)}
.about-block p{position:absolute;left:637px;width:460px;font-size:12.6px;line-height:22.5px;color:var(--text)}

/* goals */
.goal{position:absolute;top:1681px;width:197px}
.goal .fill{width:197px;height:204px}
.goal h4{font-family:"Roboto",sans-serif;font-weight:700;font-size:17px;line-height:21px;text-align:center;margin-top:18px;color:var(--ink)}

/* services */
.services{position:absolute;left:0;top:2048px;width:1200px;height:634px;background:linear-gradient(180deg,#6f93bc 0%,#4f78a8 45%,#254d7d 70%,#183a63 100%)}
.services .shade{position:absolute;left:110px;top:84px;width:420px;height:446px;background:var(--navy-soft)}
.services .card{position:absolute;left:100px;top:94px;width:430px;height:446px;background:var(--navy);color:var(--white);padding:52px 44px}
.services h2{font-size:30px;font-weight:600}
.services p{font-size:13.5px;line-height:22px;margin-top:18px}
.btn-light{position:absolute;background:var(--white);color:var(--navy);border-radius:20px;font-size:12px;display:flex;align-items:center;justify-content:center}

/* sponsors */
.sponsor{position:absolute;width:195px;height:117px;background:var(--white);display:flex;align-items:center;justify-content:center;font-weight:700;font-size:20px;color:var(--navy)}
.sponsor.sun{background:#f7c20f}
.dots{position:absolute;top:3164px;left:565px;display:flex;gap:6px}
.dots span{width:8px;height:8px;border-radius:4px;background:var(--navy)}
.dots span:first-child{width:24px}

/* practical */
.practical h2{position:absolute;left:111px;top:3300px;font-size:34px;line-height:42px;font-weight:600;width:560px}
.practical p{position:absolute;left:111px;top:3410px;width:470px;font-size:12.6px;line-height:22.6px;color:var(--text)}

/* fleet */
.fleet{position:absolute;left:0;top:3780px;width:1200px;height:418px;background:var(--navy);overflow:hidden}
.fleet .photo{left:0;top:0;width:712px;height:418px;background:linear-gradient(120deg,#c9b9a4 0%,#9c8a77 40%,#5d5a66 70%,#2f3b70 100%)}
.fleet .frame{position:absolute;left:430px;top:20px;width:753px;height:378px;border:1px solid rgba(255,255,255,.4)}
.fleet .badge{position:absolute;left:423px;top:10px;width:252px;height:252px;border-radius:50%;background:var(--red);color:var(--white);text-align:center;padding-top:58px;font-family:"Roboto",sans-serif;font-weight:700}
.fleet .badge .m{font-size:26px}
.fleet .badge .d{font-size:56px;line-height:56px}
.fleet .badge .t{font-size:17px}
.fleet .copy{position:absolute;left:703px;top:150px;width:400px;text-align:center;color:var(--white);font-family:"Roboto",sans-serif;font-size:30px;line-height:38px}
.fleet .copy b{font-weight:700}

/* gallery */
.gal{position:absolute}

/* footer */
.site-footer{position:absolute;left:0;top:4880px;width:1200px;height:438px}
.foot-brand{position:absolute;left:75px;top:177px;width:210px;height:210px;border-radius:50%;background:var(--navy);border:6px solid var(--white);display:flex;align-items:center;justify-content:center;color:var(--white);font-weight:600;font-size:20px}
.foot-col{position:absolute;top:202px;color:var(--white);font-size:11.5px}
.foot-col h5{font-size:12px;font-weight:600;margin-bottom:28px}
.foot-col ul{list-style:none}
.foot-col li{line-height:22.6px;padding-left:18px;position:relative}
.foot-col li::before{content:"";position:absolute;left:0;top:10px;width:4px;height:4px;border-radius:50%;background:var(--white)}
.foot-contact div{display:flex;gap:14px;line-height:22px}
.foot-contact svg{flex:none;margin-top:5px}
.news-input{width:259px;height:42px;border-radius:21px;background:var(--white);color:#888;font-size:11px;padding:13px 20px}
.news-btn{width:259px;height:38px;border-radius:19px;background:var(--navy);color:var(--white);font-size:12px;display:flex;align-items:center;justify-content:center;margin-top:8px}
.copyright{position:absolute;left:71px;top:5352px;font-size:11.5px;color:var(--text)}
.copyright b{color:var(--navy)}
.social{position:absolute;top:5340px;left:963px;display:flex;gap:14px}
.social span{width:34px;height:34px;border-radius:50%;background:var(--navy)}
</style>
</head>
<body>

<header class="site-header">
  <div class="brand">Sailbrightly</div>
  <div class="call">
    <span class="ico"><svg width="14" height="14" viewBox="0 0 24 24"><path fill="#fff" d="M6.6 10.8a15.1 15.1 0 006.6 6.6l2.2-2.2a1 1 0 011-.25 11.4 11.4 0 003.6.57 1 1 0 011 1V20a1 1 0 01-1 1A17 17 0 013 4a1 1 0 011-1h3.5a1 1 0 011 1c0 1.25.2 2.45.57 3.6a1 1 0 01-.25 1z"/></svg></span>
    <span>Call Us<br>0241 555 0190</span>
  </div>
  <div class="lang"><span class="flag"></span>Eng ⌄</div>
  <div class="btn-donate" style="left:965px;top:36px;width:159px;height:38px">DONATE
    <span class="arr"><svg width="36" height="12" viewBox="0 0 36 12"><path d="M0 6h33M28 1l5 5-5 5" stroke="#fff" stroke-width="1.6" fill="none"/></svg></span>
  </div>
  <nav class="main-nav">
    <a class="active" style="left:513px">Home</a>
    <a style="left:599px">About Cruises</a>
    <a style="left:733px">Sponsors</a>
    <a style="left:836px">Information</a>
    <a style="left:957px">Gallery</a>
    <a style="left:1053px">Contact us</a>
  </nav>
</header>

<section class="hero">
  <div class="photo" role="img" aria-label="Boy steering a sailing yacht at the wheel on a sunny sea with hills behind"></div>
  <div class="hero-copy">
    <div class="pre">Welcome To</div>
    <h1>Sailbrightly</h1>
    <p>community service for children with disabilities</p>
  </div>
  <div class="btn-donate" style="left:71px;top:423px;width:157px;height:41px;padding-left:30px">DONATE
    <span class="arr"><svg width="36" height="12" viewBox="0 0 36 12"><path d="M0 6h33M28 1l5 5-5 5" stroke="#fff" stroke-width="1.6" fill="none"/></svg></span>
  </div>
  <span class="slide-arrow" style="left:10px"><svg width="8" height="10"><path d="M6 1L2 5l4 4" stroke="#fff" fill="none"/></svg></span>
  <span class="slide-arrow" style="right:10px;background:var(--navy)"><svg width="8" height="10"><path d="M2 1l4 4-4 4" stroke="#fff" fill="none"/></svg></span>
  <svg class="abs" style="left:0;bottom:0" width="1200" height="150" viewBox="0 0 1200 150" preserveAspectRatio="none">
    <path d="M0 40 C250 160 520 150 760 110 C960 78 1100 60 1200 20 V150 H0Z" fill="#1c2a7a"/>
    <path d="M0 60 C250 170 520 165 760 125 C960 95 1100 80 1200 60 V150 H0Z" fill="#eaf3fb"/>
  </svg>
</section>

<h2 class="section-title" style="top:962px">About Cruises</h2>
<div class="about-block">
  <div class="framed" style="left:293px;top:1026px;width:266px;height:289px"><div class="fill" role="img" aria-label="Sailing yacht on open blue water" style="background:linear-gradient(180deg,#a9c7e4,#3f6fa6)"></div></div>
  <div class="framed" style="left:73px;top:1135px;width:201px;height:180px"><div class="fill" role="img" aria-label="Children on deck of a yacht" style="background:linear-gradient(180deg,#9fb1bf,#55677a)"></div></div>
  <div class="framed" style="left:170px;top:1344px;width:389px;height:201px"><div class="fill" role="img" aria-label="Group of children and crew posing on a harbour quay" style="background:linear-gradient(180deg,#cfd9e2,#7a6f6a)"></div></div>
  <h3 style="top:1072px">We are...</h3>
  <p style="top:1140px">trained social workers and experienced skippers who volunteer in the Sailbrightly association and organize a fleet for socially disadvantaged children and young people from central Upper Austria every year and set up the necessary financial resources.</p>
  <h3 style="top:1252px">We want...</h3>
  <p style="top:1314px">enabling children and young people who don't always have it easy in life to spend an unforgettable week in Croatia. It is precisely this shared experience that gives the children and young people a new zest for life and perspectives for their future. Through the reflection and also the care afterwards in the individual facilities, the children and young people can draw on this experience for a long time to come. This sustainability creates numerous pedagogical points of contact that represent a valuable basis for the achievement of goals.</p>
</div>

<h2 class="section-title" style="top:1624px">Project Goals</h2>
<div class="goal" style="left:73px"><div class="fill" role="img" aria-label="Girl standing on a yacht deck" style="background:linear-gradient(180deg,#8fb6d8,#3d6b98)"></div><h4>Strengthening of Self-esteem and social skills</h4></div>
<div class="goal" style="left:287px"><div class="fill" role="img" aria-label="Children sitting together on deck at sea" style="background:linear-gradient(180deg,#6e95bd,#2f5680)"></div><h4>Take responsibility for yourself and others</h4></div>
<div class="goal" style="left:500px"><div class="fill" role="img" aria-label="Inflatable toy floating on calm evening water" style="background:linear-gradient(180deg,#b8b6ad,#6b7785)"></div><h4 style="margin-top:26px">Practicing Tolerance</h4></div>
<div class="goal" style="left:714px"><div class="fill" role="img" aria-label="Group holding a trophy at an evening event" style="background:linear-gradient(180deg,#6d4a3e,#a8403a)"></div><h4>Development of non-violent conflict resolution strategies</h4></div>
<div class="goal" style="left:928px"><div class="fill" role="img" aria-label="Children playing on a harbour promenade" style="background:linear-gradient(180deg,#c7d6e6,#8d9aa6)"></div><h4>Experiential Learning</h4></div>

<section class="services" role="img" aria-label="Sailing yacht with white sails on open sea under a blue sky">
  <div class="shade"></div>
  <div class="card">
    <h2>Our Services</h2>
    <p>Lorem Ipsum is simply dummy text of the print iand typesetting industry has been the Quality dummy text ever since the 1500s,</p>
    <p>when an unknown printer took a galley of type and scrambled it to make a type specimen book. It has survived not only five centuries, but also the leap into electronic typesetting, essentially unchanged. It was popularised in the 1960s</p>
  </div>
  <div class="btn-light" style="left:145px;top:467px;width:155px;height:38px">Read More</div>
</section>

<h2 class="section-title" style="top:2765px">Sponsors</h2>
<p class="abs" style="top:2818px;left:0;width:1200px;text-align:center;font-size:12.5px;color:var(--text)">Thank you for your great commitment and support:</p>
<div class="sponsor" style="left:73px;top:2875px">Rainfield</div>
<div class="sponsor" style="left:287px;top:2875px">Stonewell</div>
<div class="sponsor" style="left:501px;top:2875px;font-size:17px">Elektro Brightmann</div>
<div class="sponsor" style="left:715px;top:2875px">Greenwalder</div>
<div class="sponsor" style="left:929px;top:2875px">Marevo</div>
<div class="sponsor" style="left:73px;top:3005px;font-size:18px">Halden Studio</div>
<div class="sponsor" style="left:287px;top:3005px">Lindfort</div>
<div class="sponsor" style="left:501px;top:3005px">Elefara</div>
<div class="sponsor" style="left:715px;top:3005px">Hubrecht</div>
<div class="sponsor sun" style="left:929px;top:3005px">SV Lakeshore</div>
<div class="dots"><span></span><span></span><span></span></div>

<div class="practical">
  <h2>Practical implementation of the pedagogical considerations</h2>
  <p>The participants are consciously involved in sailing activities. There are responsibilities for a wide variety of tasks in daily life. A cooking and cleaning plan should help to take responsibility towards the group. The fact of steering a sailing ship alone fills many with great pride. Recurring activities on the ship require the involvement of every crew member. This gives everyone the feeling of being important to the community and everyone learns to take on this responsibility if they can. Sailbrightly offers an ideal training ground for social learning. The intensive confrontation with others and the group in a confined space offers a wide variety of opportunities to try out dealing with fellow human beings. All of these experiences can lead to self-esteem.</p>
  <div class="framed" style="left:674px;top:3294px;width:450px;height:398px;padding:16px"><div class="fill" role="img" aria-label="Coastal old town with a church tower seen from the sea" style="background:linear-gradient(180deg,#9fc0e0 0%,#b9cde0 45%,#9b8f7f 58%,#2d5e96 66%,#1f4a7e 100%)"></div></div>
</div>

<section class="fleet">
  <div class="photo" role="img" aria-label="Group of men smiling with a sailing trophy"></div>
  <div class="frame"></div>
  <div class="badge"><div class="m">August</div><div class="d">28th</div><div class="t">to September 3rd.</div></div>
  <div class="copy"><b>Fleet 2022</b><br>will be held and will<br><b>take place from</b></div>
  <div class="btn-light" style="left:840px;top:291px;width:153px;height:38px">Join Us</div>
</section>

<h2 class="section-title" style="top:4267px">Gallery</h2>
<div class="gal" role="img" aria-label="Large group photo of children and crew" style="left:73px;top:4328px;width:335px;height:202px;background:linear-gradient(180deg,#a5b7c9,#3f4e67)"></div>
<div class="gal" role="img" aria-label="Children riding in an inflatable dinghy" style="left:73px;top:4557px;width:335px;height:203px;background:linear-gradient(180deg,#3b6ea3,#1d4a7c)"></div>
<div class="gal" role="img" aria-label="Girl at the helm of a yacht" style="left:431px;top:4328px;width:335px;height:432px;background:linear-gradient(180deg,#c9ccc9,#6a6a70);border:3px solid var(--navy)">
  <svg class="abs" style="left:150px;top:200px" width="34" height="34" viewBox="0 0 34 34"><path d="M2 11V2h9M23 2h9v9M32 23v9h-9M11 32H2v-9" stroke="#fff" stroke-width="2" fill="none"/></svg>
</div>
<div class="gal" role="img" aria-label="Team group photo in a hall" style="left:789px;top:4328px;width:335px;height:202px;background:linear-gradient(180deg,#b7ad9d,#4a4542)"></div>
<div class="gal" role="img" aria-label="Sponsors holding a certificate and trophy" style="left:789px;top:4557px;width:335px;height:203px;background:linear-gradient(180deg,#c94545,#7a2a30)"></div>
<div class="btn-light" style="left:521px;top:4793px;width:155px;height:36px;background:var(--navy);color:var(--white)">View More</div>

<footer class="site-footer">
  <svg class="abs" style="left:0;top:0" width="1200" height="438" viewBox="0 0 1200 438" preserveAspectRatio="none">
    <path d="M0 70 C250 10 520 20 760 60 C960 95 1100 60 1200 20 V438 H0Z" fill="#1c2a7a"/>
    <path d="M0 110 C250 50 520 60 760 95 C960 125 1100 95 1200 70 V438 H0Z" fill="#1b1d24"/>
  </svg>
  <div class="foot-brand">Sailbrightly</div>
  <div class="foot-col" style="left:385px">
    <h5>Quick Link</h5>
    <ul><li>Home</li><li>About Cruises</li><li>Sponsors</li><li>Information</li><li>Gallery</li><li>Contact us</li></ul>
  </div>
  <div class="foot-col foot-contact" style="left:580px">
    <h5>Quick Contact</h5>
    <div><svg width="10" height="13" viewBox="0 0 10 13"><path d="M5 0a5 5 0 00-5 5c0 4 5 8 5 8s5-4 5-8a5 5 0 00-5-5zm0 7a2 2 0 110-4 2 2 0 010 4z" fill="#fff"/></svg><span>45 Harbour Lane,<br>Portview 10245,<br>United States</span></div>
    <div style="margin-top:22px"><svg width="11" height="11" viewBox="0 0 24 24"><path fill="#fff" d="M6.6 10.8a15.1 15.1 0 006.6 6.6l2.2-2.2a1 1 0 011-.25 11.4 11.4 0 003.6.57 1 1 0 011 1V20a1 1 0 01-1 1A17 17 0 013 4a1 1 0 011-1h3.5a1 1 0 011 1c0 1.25.2 2.45.57 3.6a1 1 0 01-.25 1z"/></svg><span>0241 555 0190</span></div>
    <div><svg width="12" height="10" viewBox="0 0 12 10"><rect x=".5" y=".5" width="11" height="9" fill="none" stroke="#fff"/><path d="M.5 .5l5.5 5 5.5-5" fill="none" stroke="#fff"/></svg><span>info@sailbrightly.com</span></div>
  </div>
  <div class="foot-col" style="left:865px">
    <h5 style="margin-bottom:16px">Newsletter</h5>
    <div class="news-input">Your Email</div>
    <div class="news-btn">Subscribe</div>
  </div>
</footer>

<p class="copyright">Copyright © 2022 <b>SAILBRIGHTLY</b>. All Rights Reserved.</p>
<div class="social" aria-label="Social links"><span></span><span></span><span></span><span></span></div>

</body>
</html>
```